Spring FWC Lawn Care Doorhanger

I need a design for a doorhanger for a lawn care business. The door hanger should focus on the following services: Complete 6 Application Fertilization & Weed Control Program, Spring or Fall Core Aeration and Overseed.
Our business focuses on quality of service.
*Special Offer: Free Grub Control Application *with completion of new 6 app program agreement

I have attached a past version that we have used.

Font styles to use
Serif
Sans Serif

Colors
0054AA
0677BA
7BADD7
CADEEF
E8F1F8
59FF00
82FF00
B8FF75
E3FFCB
F4FFEA

```html
<!DOCTYPE html>
<html lang="en">
<head>
<meta charset="utf-8">
<title>Spring Lawn Care Door Hanger</title>
<link rel="stylesheet" href="https://fonts.googleapis.com/css2?family=Open+Sans:ital,wght@0,400;0,600;0,700;0,800;1,600&family=Kaushan+Script&display=swap">
<style>
  :root {
    --backdrop: #2b303b;
    --blue-deep: #0054aa;
    --blue-mid: #0677ba;
    --blue-soft: #7badd7;
    --green-field: #3d9a2e;
    --yellow: #ffe14d;
    --white: #ffffff;
    --sky: #dfe6ea;
    --grass: #5f9a3a;
  }
  * { box-sizing: border-box; margin: 0; padding: 0; }
  html, body { width: 1200px; height: 1200px; overflow: hidden; }
  body {
    background: var(--backdrop);
    font-family: "Open Sans", Arial, sans-serif;
    position: relative;
  }
  .door-hanger {
    position: absolute;
    left: 390px; top: 55px;
    width: 420px; height: 1090px;
    border-radius: 16px;
    overflow: hidden;
    background: var(--green-field);
  }
  .hero-photo {
    position: absolute; left: 0; top: 0;
    width: 420px; height: 420px;
    background: linear-gradient(180deg, var(--sky) 0%, #c9d2cf 32%, #8fae6f 55%, var(--grass) 100%);
  }
  .hero-curve { position: absolute; left: 0; top: 360px; width: 420px; height: 80px; }
  .door-hole {
    position: absolute; left: 110px; top: 106px;
    width: 196px; height: 196px; border-radius: 50%;
    background: var(--backdrop);
    box-shadow: 0 0 0 4px var(--white);
  }
  .brand {
    position: absolute; right: 20px; top: 20px;
    display: flex; align-items: center; gap: 8px;
  }
  .brand-dot {
    width: 14px; height: 14px; border-radius: 50%;
    background: var(--blue-deep);
  }
  .brand-name {
    color: var(--blue-deep);
    font-weight: 700; font-size: 26px; line-height: 1;
  }
  .headline {
    position: absolute; left: 0; top: 424px; width: 420px;
    text-align: center;
    color: var(--yellow);
    font-weight: 700;
    font-size: 60px;
    line-height: 62px;
  }
  .stars {
    position: absolute; left: 0; top: 554px; width: 420px;
    display: flex; justify-content: center;
  }
  .tagline {
    position: absolute; left: 20px; top: 584px; width: 380px;
    text-align: center; color: var(--white);
    font-weight: 700; font-size: 18px; line-height: 23px;
  }
  .services {
    position: absolute; left: 12px; top: 678px; width: 396px;
    display: flex; gap: 11px;
  }
  .service-card {
    position: relative;
    width: 124px; height: 216px;
    border: 3px solid var(--yellow);
    border-radius: 12px;
    overflow: hidden;
    background: linear-gradient(180deg, var(--blue-soft) 0%, var(--blue-mid) 45%, var(--blue-deep) 100%);
  }
  .service-photo { position: absolute; left: 0; top: 0; width: 100%; height: 90px; }
  .service-photo.worker { background: linear-gradient(180deg, #4d6a86, rgba(6,119,186,0)); }
  .service-photo.flowers { background: linear-gradient(180deg, #5f8f4a, rgba(6,119,186,0)); }
  .service-photo.lawn { background: linear-gradient(180deg, #9fb9c8, rgba(6,119,186,0)); }
  .service-text {
    position: absolute; left: 8px; right: 6px; top: 94px;
    color: var(--white); font-weight: 700; font-size: 14px; line-height: 19px;
  }
  .offer {
    position: absolute; left: 0; top: 904px; width: 420px; height: 118px;
    background: linear-gradient(90deg, var(--blue-deep), var(--blue-mid));
  }
  .offer-label {
    position: absolute; left: 10px; top: 34px;
    font-family: "Kaushan Script", cursive;
    color: var(--yellow); font-size: 26px; line-height: 26px;
    transform: rotate(-12deg);
  }
  .offer-free {
    position: absolute; left: 98px; top: 18px;
    color: var(--white); font-weight: 800; font-size: 52px; line-height: 56px;
  }
  .offer-item {
    position: absolute; left: 240px; top: 24px;
    color: var(--white); font-weight: 600; font-size: 22px; line-height: 24px;
  }
  .offer-note {
    position: absolute; left: 98px; top: 84px;
    color: var(--white); font-style: italic; font-weight: 600; font-size: 12px;
  }
  .contact-bar {
    position: absolute; left: 0; top: 1022px; width: 420px; height: 68px;
    display: flex; align-items: center; justify-content: space-between;
    padding: 0 14px;
  }
  .phone { color: var(--yellow); font-weight: 700; font-size: 22px; }
  .website {
    display: flex; align-items: center; gap: 6px;
    border: 2px solid var(--yellow); border-radius: 14px;
    padding: 2px 12px 2px 8px;
    color: var(--white); font-weight: 600; font-size: 17px;
  }
</style>
</head>
<body>
  <div class="door-hanger">
    <div class="hero-photo" role="img" aria-label="Lawn care technician riding a yellow aerator across a front lawn with houses behind"></div>
    <svg class="hero-curve" viewBox="0 0 420 80" preserveAspectRatio="none">
      <path d="M0 58 C 140 62 300 40 420 0 L420 80 L0 80 Z" fill="var(--blue-deep)"/>
      <path d="M0 68 C 140 72 300 52 420 14 L420 80 L0 80 Z" fill="var(--green-field)"/>
    </svg>
    <div class="door-hole"></div>
    <div class="brand">
      <span class="brand-dot"></span>
      <span class="brand-name">Fieldcrest Turf</span>
    </div>

    <h1 class="headline">Lawn Care<br>Services</h1>
    <div class="stars">
      <svg width="110" height="18" viewBox="0 0 110 18">
        <g fill="var(--yellow)">
          <polygon points="9,0 11.3,6.2 18,6.5 12.8,10.6 14.6,17 9,13.3 3.4,17 5.2,10.6 0,6.5 6.7,6.2"/>
          <polygon transform="translate(23 0)" points="9,0 11.3,6.2 18,6.5 12.8,10.6 14.6,17 9,13.3 3.4,17 5.2,10.6 0,6.5 6.7,6.2"/>
          <polygon transform="translate(46 0)" points="9,0 11.3,6.2 18,6.5 12.8,10.6 14.6,17 9,13.3 3.4,17 5.2,10.6 0,6.5 6.7,6.2"/>
          <polygon transform="translate(69 0)" points="9,0 11.3,6.2 18,6.5 12.8,10.6 14.6,17 9,13.3 3.4,17 5.2,10.6 0,6.5 6.7,6.2"/>
          <polygon transform="translate(92 0)" points="9,0 11.3,6.2 18,6.5 12.8,10.6 14.6,17 9,13.3 3.4,17 5.2,10.6 0,6.5 6.7,6.2"/>
        </g>
      </svg>
    </div>
    <p class="tagline">Give your lawn the best care possible with our high-quality lawn care services.</p>

    <div class="services">
      <div class="service-card">
        <div class="service-photo worker" role="img" aria-label="Technician spreading fertilizer"></div>
        <p class="service-text">Complete 6 Application Fertilization &amp; Weed Control Program</p>
      </div>
      <div class="service-card">
        <div class="service-photo flowers" role="img" aria-label="White flowers in a green garden"></div>
        <p class="service-text">Spring or Fall Core Aeration and Overseed</p>
      </div>
      <div class="service-card">
        <div class="service-photo lawn" role="img" aria-label="Close view of lawn equipment on grass"></div>
        <p class="service-text">Our business focuses on quality of service.</p>
      </div>
    </div>

    <div class="offer">
      <div class="offer-label">Special<br>&nbsp;Offer</div>
      <div class="offer-free">FREE</div>
      <div class="offer-item">Grub Control<br>Application</div>
      <div class="offer-note">*with completion of new 6 app program agreement</div>
    </div>

    <div class="contact-bar">
      <span class="phone">(555) 014-2736</span>
      <span class="website">
        <svg width="16" height="16" viewBox="0 0 16 16">
          <circle cx="9.5" cy="6.5" r="4.5" fill="none" stroke="var(--yellow)" stroke-width="2"/>
          <line x1="6.2" y1="9.8" x2="1.5" y2="14.5" stroke="var(--yellow)" stroke-width="2.4" stroke-linecap="round"/>
        </svg>
        fieldcrestturf.com
      </span>
    </div>
  </div>
</body>
</html>
```